General pharmacy flyer for a pharmacy. see attached files for similar flyer design
picture should be of a black person/pharmacist
Services available
Repeat Prescription collection
Emergency Contraception
Contraceptive pill
Vitamins
and more.....
Industry/Entity Type
Pharmacy

```html
<!DOCTYPE html>
<html lang="en">
<head>
<meta charset="utf-8">
<title>Oak Pharmacy Flyer</title>
<link href="https://fonts.googleapis.com/css2?family=Montserrat:wght@300;400;700&display=swap" rel="stylesheet">
<style>
  :root {
    --stage: #ef7a1a;
    --blue: #1375c1;
    --blue-deep: #0d68b0;
    --green: #3bb54a;
    --green-deep: #2fa43f;
    --white: #ffffff;
    --header-grey: #f2f2f3;
    --ink: #303236;
    --photo-a: #e9edf0;
    --photo-b: #c7ced6;
  }
  * { margin: 0; padding: 0; box-sizing: border-box; }
  html, body { width: 1200px; height: 900px; overflow: hidden; }
  body {
    background: var(--stage);
    font-family: "Montserrat", Arial, sans-serif;
    position: relative;
  }
  .flyer {
    position: absolute;
    left: 313px;
    top: 93px;
    width: 693px;
    height: 911px;
    transform: scale(0.8);
    transform-origin: 0 0;
    overflow: hidden;
    background: var(--blue);
  }
  .flyer-shapes { position: absolute; inset: 0; }
  .brand {
    position: absolute;
    left: 262px;
    top: 88px;
    display: flex;
    align-items: center;
    gap: 40px;
    white-space: nowrap;
  }
  .brand-dot {
    width: 58px; height: 58px; border-radius: 50%;
    background: var(--blue);
  }
  .brand-name {
    font-weight: 700;
    font-size: 32px;
    letter-spacing: 1px;
    color: var(--ink);
  }
  .rule {
    position: absolute;
    height: 2px;
    background: var(--white);
  }
  .rule-top { left: 35px; top: 265px; width: 196px; }
  .rule-bottom { left: 35px; top: 471px; width: 242px; }
  .headline {
    position: absolute;
    left: 35px;
    top: 289px;
    color: var(--white);
    font-weight: 700;
    font-size: 25px;
    line-height: 30.3px;
    letter-spacing: 0.5px;
    white-space: nowrap;
  }
  .services-title {
    position: absolute;
    left: 29px;
    top: 547px;
    color: var(--white);
    font-weight: 700;
    font-size: 24px;
  }
  .services-list {
    position: absolute;
    left: 20px;
    top: 584px;
    list-style: none;
    color: var(--white);
    font-weight: 400;
    font-size: 25px;
    line-height: 30.5px;
  }
  .services-list li { padding-left: 23px; position: relative; }
  .services-list li::before {
    content: "o";
    position: absolute;
    left: 0;
    font-size: 22px;
  }
  .contact {
    position: absolute;
    color: var(--white);
    font-size: 16px;
    font-weight: 400;
    line-height: 19px;
    white-space: nowrap;
  }
  .contact svg { position: absolute; }
  .contact-street { left: 399px; top: 660px; }
  .contact-street .line-two { padding-left: 6px; }
  .contact-street svg { left: -27px; top: 0; }
  .contact-town { left: 416px; top: 719px; }
  .contact-town svg { left: -34px; top: -2px; }
  .contact-phone { left: 427px; top: 758px; }
  .contact-phone svg { left: -32px; top: -2px; }
  .contact-mail { left: 438px; top: 797px; }
  .contact-mail svg { left: -38px; top: 2px; }
</style>
</head>
<body>
  <main class="flyer">
    <svg class="flyer-shapes" width="693" height="911" viewBox="0 0 693 911">
      <defs>
        <linearGradient id="photoTone" x1="0" y1="0" x2="1" y2="1">
          <stop offset="0" stop-color="var(--photo-a)"/>
          <stop offset="1" stop-color="var(--photo-b)"/>
        </linearGradient>
        <linearGradient id="edgeShade" x1="0" y1="0" x2="1" y2="0">
          <stop offset="0" stop-color="#9fa2a6"/>
          <stop offset="1" stop-color="#e6e7e8"/>
        </linearGradient>
      </defs>
      <rect class="blue-panel" width="693" height="911" fill="var(--blue)"/>
      <polygon class="blue-shade" points="0,0 184,0 250,270 0,690" fill="var(--blue-deep)"/>
      <polygon class="header-edge" points="184,0 235,0 285,206 234,206" fill="url(#edgeShade)"/>
      <polygon class="header-band" points="235,0 693,0 693,206 285,206" fill="var(--white)"/>
      <polygon class="header-tint" points="690,0 693,0 693,206 614,206" fill="var(--header-grey)"/>
      <polygon class="green-panel" points="344,626 693,626 693,911 409,911" fill="var(--green)"/>
      <polygon class="green-shade" points="344,626 400,626 460,911 409,911" fill="var(--green-deep)"/>
      <polygon class="photo" role="img" aria-label="Photo of a smiling pharmacist in a white coat standing with arms crossed in front of pharmacy shelves" points="234,206 693,206 693,626 344,626" fill="url(#photoTone)"/>
    </svg>

    <div class="brand">
      <span class="brand-dot"></span>
      <span class="brand-name">OAK PHARMACY</span>
    </div>

    <div class="rule rule-top"></div>
    <h1 class="headline">COME VISIT<br>OAK PHARMACY<br>FOR ALL YOUR<br>PRESCRIPTION<br>NEED AND MORE</h1>
    <div class="rule rule-bottom"></div>

    <h2 class="services-title">Services include</h2>
    <ul class="services-list">
      <li>Repeat prescription<br>collection</li>
      <li>Emergency<br>contraception</li>
      <li>Contraceptive pill</li>
      <li>Vitamins</li>
      <li>And More................</li>
    </ul>

    <div class="contact contact-street">
      <svg width="20" height="28" viewBox="0 0 20 28"><path d="M10 0C4.5 0 0 4.4 0 9.8 0 17 10 28 10 28s10-11 10-18.2C20 4.4 15.5 0 10 0z" fill="var(--white)"/><circle cx="10" cy="9.8" r="3.6" fill="var(--green)"/></svg>
      27 Palm Row (Corner of Palm Row<br><span class="line-two">and Bay Street)</span>
    </div>
    <div class="contact contact-town">
      <svg width="20" height="28" viewBox="0 0 20 28"><path d="M10 0C4.5 0 0 4.4 0 9.8 0 17 10 28 10 28s10-11 10-18.2C20 4.4 15.5 0 10 0z" fill="var(--white)"/><circle cx="10" cy="9.8" r="3.6" fill="var(--green)"/></svg>
      Quay Point, Seaport, St Alden
    </div>
    <div class="contact contact-phone">
      <svg width="20" height="24" viewBox="0 0 20 24"><path d="M5 1l3 5-2.5 2.5c1 3 3 6 6 8L14 14l5 3-2 5c-8 0-16-10-15-18z" fill="var(--white)"/></svg>
      555 0142
    </div>
    <div class="contact contact-mail">
      <svg width="26" height="18" viewBox="0 0 26 18"><rect x="1.2" y="1.2" width="23.6" height="15.6" fill="none" stroke="var(--white)" stroke-width="2.4"/><path d="M1.5 2l11.5 9 11.5-9" fill="none" stroke="var(--white)" stroke-width="2.4"/></svg>
      oakpharmacy@mail.com
    </div>
  </main>
</body>
</html>
```